5'x5' Banner Redesign

Looking to get a cleaner, crisper version of our banner. We would like our logo with the American flag in the background. Banner will be 5'x5'. You can use the logo and wording from the .ai file provided. Fonts are Marker Felt Wide and Times New Roman.

```html
<!DOCTYPE html>
<html lang="en">
<head>
<meta charset="utf-8">
<title>PlayWell Physical Therapy Banner</title>
<link rel="stylesheet" href="https://fonts.googleapis.com/css2?family=Permanent+Marker&display=swap">
<style>
  :root {
    --page-grey: #b3b3b3;
    --navy-deep: #111a35;
    --navy: #1c2550;
    --maroon: #6a1a3c;
    --flag-blue: #23478f;
    --flag-red: #c4122f;
    --white: #ffffff;
  }
  * { margin: 0; padding: 0; box-sizing: border-box; }
  html, body {
    width: 1200px;
    height: 1200px;
    overflow: hidden;
    background: var(--page-grey);
  }
  .banner {
    position: absolute;
    left: 201px;
    top: 201px;
    width: 800px;
    height: 800px;
    overflow: hidden;
    background: var(--navy-deep);
  }
  .flag-backdrop {
    position: absolute;
    inset: 0;
    background:
      radial-gradient(circle at 50% 52%, rgba(140, 30, 70, 0.75) 0%, rgba(90, 25, 60, 0.5) 25%, rgba(17, 26, 53, 0) 60%),
      linear-gradient(160deg, var(--navy) 0%, var(--navy-deep) 100%);
  }
  .brand-mark {
    position: absolute;
    left: 262px;
    top: 86px;
    width: 276px;
    height: 274px;
    background: var(--white);
  }
  .brand-name {
    position: absolute;
    left: 0;
    width: 100%;
    top: 388px;
    text-align: center;
    font-family: "Permanent Marker", cursive;
    font-size: 58px;
    line-height: 1;
    color: var(--white);
    letter-spacing: 2px;
  }
  .divider {
    position: absolute;
    left: 279px;
    top: 463px;
    width: 241px;
    height: 3px;
    background: var(--white);
  }
  .service-title {
    position: absolute;
    left: 0;
    width: 100%;
    top: 488px;
    text-align: center;
    font-family: "Permanent Marker", cursive;
    font-size: 94px;
    line-height: 92px;
    color: var(--white);
  }
  .flag-wave {
    position: absolute;
    left: 0;
    top: 580px;
    width: 800px;
    height: 220px;
  }
</style>
</head>
<body>
  <main class="banner">
    <div class="flag-backdrop" role="img" aria-label="Dark waving American flag backdrop"></div>

    <div class="brand-mark" aria-hidden="true"></div>
    <p class="brand-name">PlayWell</p>
    <div class="divider"></div>

    <h1 class="service-title">PHYSICAL<br>THERAPY</h1>

    <svg class="flag-wave" viewBox="0 0 800 220" role="img" aria-label="Waving American flag ribbon">
      <defs>
        <linearGradient id="flagRibbon" x1="0" y1="0" x2="1" y2="0">
          <stop offset="0" stop-color="var(--flag-blue)"/>
          <stop offset="0.35" stop-color="#7f6a8f"/>
          <stop offset="1" stop-color="var(--flag-red)"/>
        </linearGradient>
      </defs>
      <path d="M0 10 C120 70 260 160 420 168 C560 172 680 90 800 60 L800 175 C650 185 520 190 400 200 C260 212 120 220 0 220 Z" fill="url(#flagRibbon)"/>
    </svg>
  </main>
</body>
</html>
```